Business Card Design Project

Design business card based on logo provided.

Industry/Entity Type

Business

Requirements
Nice to have
• Logo to be provided.

Solid green second side with reverse logo (buildings only, not text).

Because the logo is linear I think that it might be possible to extend the logo lines across the card (only on the second side) as an interesting design element.

"Helping Owners Build Better Building Programs"

"Job Order Contracting and Best Value Specialist"

"Cooperation - Innovation - Efficiency"

Basic Info:
Nora Whitfield
Owner/Founder
505-718-6024
nora@norawhitfieldpartners.example

www.norawhitfieldpartners.example (this should probably be on reverse)

```html
<!DOCTYPE html>
<html lang="en">
<head>
<meta charset="utf-8">
<title>Nora Whitfield Partners – Business Card</title>
<link rel="stylesheet" href="https://fonts.googleapis.com/css2?family=Roboto+Condensed:wght@300;400;700&display=swap">
<style>
  :root {
    --backdrop: #8a8a86;
    --green-light: #9cbc3c;
    --green-dark: #3e5b26;
    --paper: #f4f5f4;
    --ink: #2f3033;
    --ink-soft: #4a4b4e;
    --band: #3b3c40;
    --brand-green: #6b8f2c;
    --white: #ffffff;
  }
  * { box-sizing: border-box; margin: 0; padding: 0; }
  html, body {
    width: 1200px;
    height: 792px;
    overflow: hidden;
    background: var(--backdrop);
    font-family: "Roboto Condensed", Arial, sans-serif;
  }
  .sheet {
    position: relative;
    width: 1200px;
    height: 792px;
    display: flex;
    align-items: center;
    justify-content: center;
    gap: 40px;
  }
  .card {
    position: relative;
    width: 540px;
    height: 309px;
    overflow: hidden;
    box-shadow: 0 6px 18px rgba(0,0,0,0.25);
  }

  /* Reverse side */
  .card--reverse {
    background: linear-gradient(170deg, var(--green-light) 0%, var(--green-dark) 100%);
    color: var(--white);
  }
  .brand--reverse {
    position: absolute;
    right: 34px;
    top: 40px;
    display: flex;
    align-items: center;
    gap: 10px;
    font-weight: 400;
    font-size: 20px;
    letter-spacing: 1px;
    text-transform: uppercase;
    white-space: nowrap;
    color: var(--white);
  }
  .values {
    position: absolute;
    left: 34px;
    top: 132px;
    font-weight: 300;
    font-size: 17px;
    letter-spacing: 0.5px;
    white-space: nowrap;
  }
  .website {
    position: absolute;
    left: 34px;
    bottom: 26px;
    font-weight: 300;
    font-size: 14px;
    letter-spacing: 2px;
    white-space: nowrap;
  }
  .brand-square {
    width: 14px;
    height: 14px;
    flex: none;
    background: currentColor;
  }

  /* Front side */
  .card--front {
    background: var(--paper);
    color: var(--ink);
  }
  .identity {
    position: absolute;
    left: 140px;
    top: 42px;
    width: 160px;
    text-align: right;
  }
  .person-name {
    font-weight: 700;
    font-size: 18px;
    color: var(--ink);
  }
  .person-role {
    font-weight: 400;
    font-size: 12px;
    color: var(--ink-soft);
    margin-top: 2px;
  }
  .divider {
    position: absolute;
    left: 312px;
    top: 42px;
    width: 1px;
    height: 64px;
    background: var(--ink);
  }
  .contact {
    position: absolute;
    left: 324px;
    top: 68px;
    font-style: normal;
    font-size: 12.5px;
    line-height: 17px;
    color: var(--ink);
    white-space: nowrap;
  }
  .specialty-band {
    position: absolute;
    left: 140px;
    right: 0;
    top: 112px;
    height: 22px;
    background: var(--band);
    color: var(--white);
    font-size: 13px;
    line-height: 22px;
    padding-left: 12px;
    white-space: nowrap;
  }
  .brand--front {
    position: absolute;
    left: 30px;
    bottom: 56px;
    display: flex;
    align-items: center;
    gap: 10px;
    font-weight: 400;
    font-size: 24px;
    letter-spacing: 0.5px;
    text-transform: uppercase;
    white-space: nowrap;
    color: var(--brand-green);
  }
</style>
</head>
<body>
  <main class="sheet">
    <section class="card card--reverse" aria-label="Card reverse side">
      <div class="brand brand--reverse"><span class="brand-square"></span>Nora Whitfield Partners</div>
      <p class="values">COOPERATION | INNOVATION | EFFICIENCY</p>
      <p class="website">www.norawhitfieldpartners.example</p>
    </section>

    <section class="card card--front" aria-label="Card front side">
      <div class="identity">
        <p class="person-name">Nora Whitfield</p>
        <p class="person-role">Owner/Founder</p>
      </div>
      <span class="divider"></span>
      <address class="contact">
        505-718-6024<br>
        nora@norawhitfieldpartners.example
      </address>
      <p class="specialty-band">Job Order Contracting and Best Value Implementation</p>
      <div class="brand brand--front"><span class="brand-square"></span>Nora Whitfield Partners</div>
    </section>
  </main>
</body>
</html>
```